Web Page for marketing online agency

We are an online marketing agency that is acing the direct response model. We engage with our customers throughout different marketing techniques as research copy-writing, advertisements and content writing. We would need a website design that will have four main aspects: The Vision; stating who we are, The Mission; stating what we do, The Team And It's Values, and a Contact Form. For this design we would want a sharp, clean and smart approach, with illustrated elements or suggestive images. You can use the attached copy, the logo, the USP and the motto. Please integrate them as you see fit while keeping in mind the previous needs and copy. This website is going to be our connection with our possible partners, future colleagues and even our clients. You may submit a design for one page or integrate the 4 different aspects on separate web pages.
Target Market(s)
business partners, future employees, age range 25-60
Industry/Entity Type
Direct Marketing
Number of Pages Required
1 page
Requirements
Must have
- Menu / Header
- 4 Parts or 4 Pages including: vision, mission, team, contact
- Logo
- Motto: Direct Brilliance
- USP: We help people help themselves.
- The copy attached
Nice to have
- Representative illustrated images or elements
Should not have
- A boring design, classical design - Pagequill like

```html
<!DOCTYPE html>
<html lang="en">
<head>
<meta charset="utf-8">
<title>NovaKin – Direct Brilliance</title>
<link rel="stylesheet" href="https://fonts.googleapis.com/css2?family=Arimo:wght@400;700&family=Open+Sans:wght@400;600&display=swap">
<style>
:root{
  --ink:#111111;
  --white:#ffffff;
  --blue:#2a9fd6;
  --grey-text:#555555;
  --grey-dark:#4a4a4a;
  --grey-footer:#5a5a5a;
  --line:#d6d6d6;
  --black:#000000;
}
*{box-sizing:border-box;margin:0;padding:0}
html,body{width:1200px;height:2426px;overflow:hidden;background:var(--white)}
body{position:relative;font-family:"Arimo",Arial,sans-serif;color:var(--ink)}

/* Header */
.site-header{position:absolute;left:0;top:0;width:1200px;height:78px;background:var(--white)}
.brand{position:absolute;left:50px;top:14px;display:flex;align-items:center;gap:8px}
.brand-name{font-size:30px;font-weight:700;color:var(--ink);letter-spacing:.5px}
.brand-dot{width:26px;height:26px;border-radius:50%;background:var(--blue)}
.main-nav{position:absolute;left:243px;top:0;display:flex;height:70px}
.main-nav a{width:188px;height:70px;border:1px solid #e6e6e6;border-top:none;display:flex;align-items:center;justify-content:center;font-size:13px;color:#333;text-decoration:none}

/* Hero */
.hero{position:absolute;left:0;top:78px;width:1200px;height:548px}
.hero-photo{position:absolute;inset:0;background:linear-gradient(135deg,#6b5e52 0%,#a7a39c 35%,#d9d7d2 60%,#8e8a84 100%)}
.hero-shade{position:absolute;inset:0;background:rgba(0,0,0,.18)}
.hero-title{position:absolute;left:0;width:1200px;top:208px;text-align:center;color:var(--white);font-size:27px;font-weight:700}
.hero-motto{position:absolute;left:0;width:1200px;top:244px;text-align:center;color:var(--white);font-size:19px;font-weight:700}
.hero-cta{position:absolute;left:545px;top:284px;width:114px;height:32px;border:1px solid var(--white);color:var(--white);font-size:11px;font-weight:700;display:flex;align-items:center;justify-content:center}
.hero-intro{position:absolute;left:420px;width:360px;top:480px;text-align:center;color:var(--white);font-size:11px;font-weight:700;line-height:1.3}

/* Clients */
.clients-title{position:absolute;left:0;width:1200px;top:666px;text-align:center;font-size:22px;font-weight:700;color:var(--grey-text)}
.clients-sub{position:absolute;left:0;width:1200px;top:697px;text-align:center;font-size:10px;color:var(--grey-text)}
.client{position:absolute;width:300px;display:flex;align-items:center;justify-content:center;gap:8px;font-size:24px;font-weight:700}
.client-mark{width:22px;height:22px;border-radius:50%}
.work-btn{position:absolute;left:530px;top:998px;width:110px;height:42px;border:1px solid #8a8a8a;display:flex;align-items:center;justify-content:center;font-size:11px;font-weight:700;color:#666}
.rule{position:absolute;left:0;width:1200px;height:3px;background:var(--line)}

/* Services */
.services-kicker{position:absolute;left:0;width:1200px;top:1102px;text-align:center;font-size:29px;font-weight:700;color:var(--blue)}
.services-lead{position:absolute;left:0;width:1200px;top:1145px;text-align:center;font-size:29px;color:var(--ink)}
.service{position:absolute;top:1198px;height:362px;color:var(--white)}
.service-info{left:0;width:406px;background:var(--black)}
.service-content{left:406px;width:407px;background:var(--blue)}
.service-research{left:813px;width:387px;background:var(--grey-dark)}
.service h3{position:absolute;top:30px;left:0;right:0;text-align:center;font-size:31px;font-weight:700}
.service-info h3,.service-info p{color:var(--blue)}
.service p{position:absolute;top:92px;left:30px;right:30px;font-size:21px;font-weight:700;line-height:1.25}
.service-btn{position:absolute;top:227px;left:50%;transform:translateX(-50%);width:206px;height:58px;border:1.5px solid var(--white);display:flex;align-items:center;justify-content:center;font-size:21px;color:var(--white)}

.masters-title{position:absolute;left:0;width:1200px;top:1590px;text-align:center;font-size:26px;font-weight:700;color:#444}
.masters-sub{position:absolute;left:0;width:1200px;top:1628px;text-align:center;font-size:20px;color:#444}

/* Team */
.team{position:absolute;left:0;top:1698px;width:1200px;height:534px}
.team-intro{position:absolute;left:0;top:0;width:401px;height:534px;background:var(--black);color:var(--white);text-align:center}
.team-intro h2{margin-top:44px;font-size:32px;font-weight:700}
.team-intro p{margin:34px 36px 0;font-size:21px;font-weight:700;line-height:1.25}
.team-more{position:absolute;left:0;right:0;top:364px;font-size:22px;font-weight:700}
.team-photo{position:absolute;top:0;height:534px}
.team-photo-one{left:401px;width:412px;background:linear-gradient(180deg,#e9ecef 0%,#b9bcc0 45%,#2b2e33 100%)}
.team-photo-two{left:813px;width:387px;background:linear-gradient(180deg,#3a2b22 0%,#7a5a48 40%,#2a2421 100%)}

/* Social */
.social{position:absolute;left:0;top:2252px;width:1200px;display:flex;justify-content:center;gap:26px}
.social span{font-size:14px;font-weight:700;color:var(--blue)}

/* Footer */
.site-footer{position:absolute;left:0;top:2296px;width:1200px;height:130px;background:var(--grey-footer);color:var(--white);font-family:"Open Sans",Arial,sans-serif;font-size:11px;line-height:1.3}
.footer-col{position:absolute;top:27px}
.footer-copy{position:absolute;left:133px;top:99px}
.footer-brand{position:absolute;left:730px;top:40px;display:flex;align-items:center;gap:8px}
.footer-brand .brand-name{font-family:"Arimo",Arial,sans-serif;font-size:30px;color:var(--black)}
.footer-nav{position:absolute;left:733px;top:99px;font-size:11px;word-spacing:2px}
</style>
</head>
<body>

<header class="site-header">
  <div class="brand"><span class="brand-name">NovaKin</span><span class="brand-dot"></span></div>
  <nav class="main-nav">
    <a>Home</a><a>What is NovaKin</a><a>What we do</a><a>Our Team</a><a>Contact Us</a>
  </nav>
</header>

<section class="hero">
  <div class="hero-photo" role="img" aria-label="Team celebrating in a bright open-plan office"></div>
  <div class="hero-shade"></div>
  <h1 class="hero-title">WE HELP PEOPLE HELP THEMSELVES</h1>
  <p class="hero-motto">NovaKin - Direct Brilliance</p>
  <a class="hero-cta">CALL TO ACTION</a>
  <p class="hero-intro">We are a direct response company that creates and sells information products and services that millions of people find interesting and important in their lives.</p>
</section>

<h2 class="clients-title">We love our clients</h2>
<p class="clients-sub">Our clients come first at NovaKin, and we are proud to work with some of the world's best know brands</p>

<div class="client" style="left:117px;top:772px;color:#c9302c"><span class="client-mark" style="background:#c9302c"></span>Tapmarket</div>
<div class="client" style="left:443px;top:772px;color:#111">Voltra</div>
<div class="client" style="left:788px;top:772px;color:#111">Outlastpedia</div>
<div class="client" style="left:117px;top:874px;color:#111"><span class="client-mark" style="background:#c9302c"></span>Self Reliant News</div>
<div class="client" style="left:443px;top:874px;color:#4f8a3a">Greenrow Farms</div>
<div class="client" style="left:788px;top:874px;color:#1d4f9c"><span class="client-mark" style="background:#c9302c"></span>Hartley Motors</div>

<a class="work-btn">View Our Work</a>
<div class="rule" style="top:1084px"></div>

<h2 class="services-kicker">WHAT IS IT WE DO?</h2>
<p class="services-lead">We live and breathe direct response marketing</p>

<article class="service service-info">
  <h3>INFORMATION</h3>
  <p>We create and aggregate great information products.</p>
  <a class="service-btn">Information service</a>
</article>
<article class="service service-content">
  <h3>CONTENT</h3>
  <p>We write content that compels people to act.</p>
  <a class="service-btn">Content Writing</a>
</article>
<article class="service service-research">
  <h3>RESEARCH</h3>
  <p>We do deep research to offer simple quick and easy solutions to people's most serious problems.</p>
  <a class="service-btn">Research Service</a>
</article>

<h2 class="masters-title">We are masters of direct response marketing</h2>
<p class="masters-sub">We create content and build solutions to profound challenges for millions of people</p>
<div class="rule" style="top:1694px"></div>

<section class="team">
  <div class="team-intro">
    <h2>MEET THE TEAM</h2>
    <p>We're a small team of smart, funny hard-working specialists who are pushing to become the #1 company in self-reliance. High ambition, radical honesty and a result-oriented mindset are encouraged at NovaKin.</p>
    <a class="team-more">Read more</a>
  </div>
  <div class="team-photo team-photo-one" role="img" aria-label="Portrait of a team member in a dark polo shirt"></div>
  <div class="team-photo team-photo-two" role="img" aria-label="Portrait of a team member in a shirt and waistcoat"></div>
</section>

<div class="social"><span>Linkbook</span><span>Photogram</span><span>Chirper</span></div>

<footer class="site-footer">
  <div class="footer-col" style="left:133px">CONTACT US<br>CALL<br>077482</div>
  <div class="footer-col" style="left:275px">NovaKin<br>Strada Lalelelor<br>Bucuresti</div>
  <div class="footer-col" style="left:417px">* Terms of Service<br>* Privacy Policy<br>* Hours</div>
  <div class="footer-copy">© NovaKin</div>
  <div class="footer-brand"><span class="brand-name">NovaKin</span><span class="brand-dot"></span></div>
  <div class="footer-nav">HOME | WHAT WE DO | OUR TEAM | CLIENTS | CONTACT</div>
</footer>

</body>
</html>
```